VORLEN Website Design

We need a website designed for our company VORLEN. We are a luxury lifestyle club that will provide benefits and services for our members. The site should be clean & sleek, preferably using black and white (or darker colors). (example sites: brimvale.example, tusko.example)

Here is a link of a sample page I did using wix. (https://pelmundry4.sitebuild.example/mypage) This can be used to get a general idea.

Target Market(s)

Upper Middle Class in the United States

Number of Pages Required

5+ page

Font styles to use
Sans Serif
Other font styles liked:
• Arial (or other similar fonts)

Requirements
Must have
• A clean design that is eye-catching and speaks to our company.
Nice to have
• Ideas for copy.

```html
<!DOCTYPE html>
<html lang="en">
<head>
<meta charset="utf-8">
<title>VORLEN — The Ultimate Full Service Lifestyle Club</title>
<link rel="stylesheet" href="https://fonts.googleapis.com/css2?family=Oswald:wght@400;500&family=Quicksand:wght@400;500;600;700&display=swap">
<style>
:root{
  --red:#c0392b;
  --red-dark:#a93024;
  --ink:#1e1e1e;
  --black:#000;
  --white:#fff;
  --text:#333;
  --muted:#555;
  --field:#efefef;
  --line:#d8d8d8;
  --body-font:"Quicksand",Arial,sans-serif;
  --condensed:"Oswald",Arial,sans-serif;
}
*{box-sizing:border-box;margin:0;padding:0}
html,body{width:1200px;height:4082px;overflow:hidden}
body{position:relative;background:var(--white);font-family:var(--body-font);color:var(--text)}
.abs{position:absolute}
.brand{font-family:var(--body-font);font-weight:700;color:var(--red);display:flex;align-items:center;gap:14px}
.brand-mark{width:22px;height:22px;background:var(--red);display:inline-block}

/* nav */
.site-nav{left:0;top:0;width:1200px;height:114px;background:var(--black)}
.site-nav .brand{position:absolute;left:49px;top:34px;font-size:40px}
.nav-link{position:absolute;top:53px;font-size:15px;font-weight:600;color:var(--white);letter-spacing:.5px}
.nav-link.is-active{color:var(--red)}
.nav-apply{position:absolute;left:1023px;top:44px;width:133px;height:40px;border:2px solid var(--white);border-radius:20px;background:var(--red);color:var(--white);font-size:15px;font-weight:700;display:flex;align-items:center;justify-content:center}

/* hero */
.hero-photo{left:0;top:114px;width:1200px;height:600px;background:linear-gradient(120deg,#3a3230 0%,#6b5a50 35%,#a89888 55%,#4a3e38 80%,#2a2422 100%);clip-path:polygon(0 0,100% 0,100% 516px,0 586px)}
.hero-copy{left:0;top:250px;width:1200px;text-align:center;color:var(--white)}
.hero-kicker{font-size:38px;font-weight:700;letter-spacing:2px}
.hero-title{font-family:var(--condensed);font-size:58px;font-weight:400;margin-top:2px;line-height:1.2}
.btn-red{background:var(--red);color:var(--white);border-radius:26px;display:flex;align-items:center;justify-content:center;font-weight:500}
.hero-cta{left:457px;top:403px;width:286px;height:51px;font-size:26px}

.intro-band{left:0;top:630px;width:1200px;height:405px;background:var(--red);clip-path:polygon(0 70px,100% 0,100% 335px,0 405px)}
.intro-text{left:120px;top:752px;width:960px;text-align:center;color:var(--white);font-size:22px;line-height:1.3;font-weight:500}
.btn-outline{left:479px;top:857px;width:242px;height:46px;border:2px solid var(--white);border-radius:23px;color:var(--white);font-size:22px;display:flex;align-items:center;justify-content:center;font-weight:500}

/* section headings */
.section-title{left:0;width:1200px;display:flex;justify-content:center;align-items:center;gap:16px;font-size:52px;font-weight:500;color:var(--ink)}
.section-title .accent{color:var(--red)}
.section-sub{left:0;width:1200px;text-align:center;font-size:20px;font-weight:500;color:var(--text)}

/* services */
.service-card{top:1300px;width:308px;height:327px;background:var(--white);border-radius:8px;box-shadow:0 2px 12px rgba(0,0,0,.22);padding:14px}
.service-photo{width:280px;height:208px}
.service-label{display:flex;align-items:center;justify-content:center;gap:14px;margin-top:30px;font-family:var(--condensed);font-size:24px;color:var(--ink)}
.service-label svg{flex:none}
.carousel-arrow{top:1432px;width:44px;height:64px;background:#ececec;display:flex;align-items:center;justify-content:center}

/* benefits */
.benefits-band{left:0;top:1714px;width:1200px;height:776px;background:var(--ink);clip-path:polygon(0 56px,100% 0,100% 711px,0 776px)}
.benefits-title{top:1880px;color:var(--white)}
.benefit-text{color:var(--white);font-size:18px;line-height:1.32;font-weight:500}

/* contact */
.field{background:var(--field);color:#666;font-size:17px;padding:12px 18px;font-weight:500}
.send-btn{left:482px;top:2966px;width:236px;height:46px;font-size:22px}

/* newsletter */
.news-band{left:0;top:3102px;width:1200px;height:463px;background:var(--red);clip-path:polygon(0 68px,100% 0,100% 408px,0 463px)}
.news-title{left:0;top:3214px;width:1200px;text-align:center;color:var(--white);font-size:50px;font-weight:500}
.news-text{left:0;top:3320px;width:1200px;text-align:center;color:var(--white);font-size:19px;font-weight:500}
.news-art{left:880px;top:3250px;width:200px;height:200px;border-radius:12px;background:radial-gradient(circle at 50% 45%,rgba(255,255,255,.16) 0%,rgba(255,255,255,0) 70%)}
.news-input{left:378px;top:3401px;width:444px;height:49px;border-radius:25px;background:linear-gradient(180deg,#fff 0%,#d9d9d9 100%);box-shadow:0 3px 6px rgba(0,0,0,.3)}
.news-input span{position:absolute;left:22px;top:12px;font-family:var(--condensed);font-size:20px;color:#222}
.news-go{position:absolute;right:14px;top:8px;width:33px;height:33px;border-radius:50%;background:#222;display:flex;align-items:center;justify-content:center}

/* footer */
.footer-brand{left:0;top:3618px;width:1200px;justify-content:center;font-size:46px}
.footer-col{top:3742px}
.footer-col h4{font-family:var(--condensed);font-weight:400;font-size:22px;color:var(--ink);padding-bottom:8px;border-bottom:1px solid var(--line);margin-bottom:14px}
.footer-col li{list-style:none;font-size:15px;line-height:22px;color:var(--text);font-weight:500}
.contact-row{display:flex;gap:10px;font-size:15px;line-height:22px;font-weight:500;margin-bottom:16px}
.social-row{display:flex;align-items:center;gap:12px;font-size:16px;margin-bottom:16px;font-weight:500}
.social-dot{width:22px;height:22px;border-radius:50%;background:#3a6aa8}
.foot-input{width:263px;height:32px;border-radius:16px;background:var(--field);font-size:14px;padding:7px 16px;color:#555;margin-top:12px}
.foot-sub{width:128px;height:30px;border-radius:15px;background:var(--red);color:var(--white);font-size:13px;font-weight:700;display:flex;align-items:center;justify-content:center;margin-top:20px}
.copyright{left:0;top:4022px;width:1200px;height:46px;background:var(--black);color:var(--white);font-size:13px;display:flex;align-items:center;justify-content:center;font-weight:500}
</style>
</head>
<body>

<header class="abs site-nav">
  <div class="brand"><span class="brand-mark"></span>Vorlen</div>
  <span class="nav-link is-active" style="left:497px">HOME</span>
  <span class="nav-link" style="left:590px">ABOUT</span>
  <span class="nav-link" style="left:688px">SERVICES</span>
  <span class="nav-link" style="left:803px">BENEFITS</span>
  <span class="nav-link" style="left:921px">CONTACT</span>
  <span class="nav-apply">APPLY NOW</span>
</header>

<div class="abs hero-photo" role="img" aria-label="Photo of well-dressed members mingling with wine glasses at a club event"></div>
<div class="abs hero-copy">
  <div class="hero-kicker">WELCOME TO VORLEN</div>
  <h1 class="hero-title">The Ultimate Full Service Lifestyle Club</h1>
</div>
<div class="abs btn-red hero-cta">Get Started</div>

<section class="abs intro-band"></section>
<p class="abs intro-text">VORLEN is a members only lifestyle club founded in order to bring the best services, experiences, and opportunities to our diverse community of members. Our members consist of creatives, athletes, artists, and other professionals.</p>
<div class="abs btn-outline">Learn More</div>

<h2 class="abs section-title" style="top:1140px"><span class="brand-mark"></span><span><span class="accent">Vorlen</span> Services</span></h2>
<p class="abs section-sub" style="top:1240px">VORLEN membership provides you with amazing benefits and services.</p>

<div class="abs carousel-arrow" style="left:0;border-radius:0 32px 32px 0"><svg width="12" height="18" viewBox="0 0 12 18"><path d="M9 2 3 9l6 7" fill="none" stroke="#999" stroke-width="2.5"/></svg></div>
<div class="abs carousel-arrow" style="left:1156px;border-radius:32px 0 0 32px"><svg width="12" height="18" viewBox="0 0 12 18"><path d="M3 2l6 7-6 7" fill="none" stroke="#999" stroke-width="2.5"/></svg></div>

<article class="abs service-card" style="left:100px">
  <div class="service-photo" role="img" aria-label="Photo of a grand manor house with lawn and trees" style="background:linear-gradient(180deg,#9fc2e4 0%,#c9c2b0 45%,#6e8a4a 75%,#3f5e2c 100%)"></div>
  <div class="service-label"><svg width="40" height="30" viewBox="0 0 40 30"><path d="M2 14 20 2l18 12v14H2z" fill="var(--red)"/><rect x="8" y="16" width="6" height="6" fill="#fff"/><rect x="26" y="16" width="6" height="6" fill="#fff"/><rect x="17" y="18" width="6" height="10" fill="#fff"/></svg>Real Estate Services</div>
</article>
<article class="abs service-card" style="left:443px">
  <div class="service-photo" role="img" aria-label="Photo of hands working through financial documents" style="background:linear-gradient(135deg,#dfe8f0 0%,#b7c6d4 50%,#e9e4de 100%)"></div>
  <div class="service-label"><svg width="40" height="30" viewBox="0 0 40 30"><rect x="2" y="14" width="6" height="14" fill="var(--red)"/><rect x="10" y="6" width="6" height="22" fill="var(--red)"/><rect x="18" y="10" width="6" height="18" fill="var(--red)"/><rect x="26" y="12" width="12" height="16" fill="none" stroke="var(--red)" stroke-width="2.5"/></svg>Accounting Services</div>
</article>
<article class="abs service-card" style="left:792px">
  <div class="service-photo" role="img" aria-label="Photo of a private jet parked on a runway" style="background:linear-gradient(180deg,#9aa4ad 0%,#c5cbd0 50%,#5a5f63 80%,#3e4245 100%)"></div>
  <div class="service-label"><svg width="44" height="20" viewBox="0 0 44 20"><path d="M2 10c10-3 28-4 40-1-6 3-26 4-40 1zm14-1 6-7h4l-3 7zm0 2 6 7h4l-3-7z" fill="var(--red)"/></svg>Private Jet Travel</div>
</article>

<section class="abs benefits-band"></section>
<h2 class="abs section-title benefits-title"><span class="brand-mark" style="background:var(--white)"></span><span style="color:var(--white)">Benefits</span></h2>

<svg class="abs" style="left:300px;top:1940px" width="600" height="400" viewBox="0 0 600 400" aria-hidden="true">
  <circle cx="299" cy="196" r="155" fill="none" stroke="#8a8a8a" stroke-width="5"/>
  <circle cx="299" cy="196" r="130" fill="#3a1e1c"/>
  <g stroke="#cfcfcf" stroke-width="2">
    <line x1="108" y1="87" x2="190" y2="87"/>
    <line x1="489" y1="87" x2="410" y2="87"/>
    <line x1="89" y1="291" x2="170" y2="291"/>
    <line x1="511" y1="291" x2="430" y2="291"/>
  </g>
  <g fill="var(--red)" stroke="#fff" stroke-width="3">
    <circle cx="190" cy="87" r="8"/><circle cx="410" cy="87" r="8"/>
    <circle cx="170" cy="291" r="8"/><circle cx="430" cy="291" r="8"/>
    <circle cx="108" cy="87" r="40"/><circle cx="489" cy="87" r="40"/>
    <circle cx="89" cy="291" r="40"/><circle cx="511" cy="291" r="40"/>
  </g>
  <g fill="none" stroke="#fff" stroke-width="2.5">
    <rect x="94" y="71" width="28" height="32" rx="3"/><line x1="100" y1="82" x2="116" y2="82"/><line x1="100" y1="90" x2="116" y2="90"/>
    <path d="M477 75l24 24M501 75l-24 24"/><circle cx="489" cy="87" r="6"/>
    <rect x="76" y="275" width="26" height="32" rx="3"/><path d="M82 292l5 5 10-10"/>
    <rect x="495" y="277" width="32" height="28" rx="3"/><line x1="495" y1="285" x2="527" y2="285"/><line x1="503" y1="272" x2="503" y2="281"/><line x1="519" y1="272" x2="519" y2="281"/>
  </g>
  <text x="299" y="212" text-anchor="middle" font-family="Quicksand, Arial, sans-serif" font-weight="700" font-size="46" fill="var(--red)">Vorlen</text>
</svg>

<p class="abs benefit-text" style="left:103px;top:1990px;width:260px">Members receive access to the best accountants, attorneys, real estate agents, private bankers/ advisers and more.</p>
<p class="abs benefit-text" style="left:852px;top:1990px;width:280px">Members are also provided access to exclusive venues and events from our partners.</p>
<p class="abs benefit-text" style="left:73px;top:2190px;width:270px">Members receive access to private flight travel, premium luxury gym memberships, private social clubs, and private investment opportunities.</p>
<p class="abs benefit-text" style="left:876px;top:2190px;width:250px">VORLEN organizes and supports a ton of private events and parties for our members.</p>

<h2 class="abs section-title" style="top:2592px"><span class="brand-mark"></span><span><span class="accent">Contact</span> Us</span></h2>
<p class="abs section-sub" style="top:2694px;font-size:18px">Let us know what you need.</p>
<div class="abs field" style="left:114px;top:2756px;width:316px;height:47px">Your Name</div>
<div class="abs field" style="left:444px;top:2756px;width:312px;height:47px">Your Email</div>
<div class="abs field" style="left:770px;top:2756px;width:313px;height:47px">Your Subject</div>
<div class="abs field" style="left:114px;top:2819px;width:969px;height:133px">Message</div>
<div class="abs btn-red send-btn">Send Message</div>

<section class="abs news-band"></section>
<div class="abs news-art" role="img" aria-label="Line illustration of a paper plane with a looping flight trail"></div>
<h2 class="abs news-title">Newsletter Subscription</h2>
<p class="abs news-text">Register your email address to get more information about us and our promotion</p>
<div class="abs news-input"><span>Enter Your Email Address</span><div class="news-go"><svg width="14" height="14" viewBox="0 0 14 14"><path d="M4 2l6 5-6 5" fill="none" stroke="#fff" stroke-width="2.5"/></svg></div></div>

<div class="abs brand footer-brand"><span class="brand-mark"></span>Vorlen</div>

<div class="abs footer-col" style="left:82px;width:130px">
  <h4>Quick Links</h4>
  <ul><li>Home</li><li>About</li><li>Services</li><li>Benefits</li><li>Contact</li><li>Apply Now</li></ul>
</div>
<div class="abs footer-col" style="left:240px;width:125px">
  <h4>About</h4>
  <ul><li>Company</li><li>Mission</li><li>Vision</li></ul>
</div>
<div class="abs footer-col" style="left:395px;width:210px">
  <h4>Contact</h4>
  <div class="contact-row"><svg width="16" height="20" viewBox="0 0 16 20"><path d="M8 1a6 6 0 0 0-6 6c0 5 6 12 6 12s6-7 6-12a6 6 0 0 0-6-6z" fill="none" stroke="#333" stroke-width="2"/><circle cx="8" cy="7" r="2" fill="#333"/></svg><span>48 Halden Row<br>Suite #200<br>Los Angeles, CA 90011</span></div>
  <div class="contact-row"><svg width="18" height="18" viewBox="0 0 18 18"><circle cx="9" cy="9" r="8" fill="none" stroke="#333" stroke-width="1.6"/><path d="M6 5l2 2-1 1c1 2 2 3 3 3l1-1 2 2-1 1c-3 0-7-4-7-7z" fill="#333"/></svg><span>1800.555.0142</span></div>
  <div class="contact-row"><svg width="18" height="18" viewBox="0 0 18 18"><circle cx="9" cy="9" r="8" fill="none" stroke="#333" stroke-width="1.6"/><rect x="5" y="6" width="8" height="6" fill="none" stroke="#333" stroke-width="1.4"/><path d="M5 6l4 3 4-3" fill="none" stroke="#333" stroke-width="1.4"/></svg><span>info@vorlenclub.example</span></div>
</div>
<div class="abs footer-col" style="left:667px;width:130px">
  <h4>Follow Us</h4>
  <div class="social-row"><span class="social-dot"></span>Friendspace</div>
  <div class="social-row"><span class="social-dot" style="background:#3aa0e0"></span>Chirpline</div>
  <div class="social-row"><span class="social-dot" style="background:#6a5a50"></span>Snapgram</div>
</div>
<div class="abs footer-col" style="left:857px;width:270px">
  <h4>Newsletter</h4>
  <p style="font-size:15px;line-height:20px;font-weight:500">Register your email address to get more information about us</p>
  <div class="foot-input">Email Address</div>
  <div class="foot-sub">SUBSCRIBE</div>
</div>

<footer class="abs copyright">© 2018 Vorlen Luxury Lifestyle Club. All Rights Reserved.</footer>

</body>
</html>
```